A flyer for future customers to get acquainted with our company

The flyer/card is intended for intermediaries. The purpose of this flyer is to introduce businesses to Dovrel.

It should convey: real estate and financing, with actual images. Various keywords describing what we do: project financing, temporary real estate financing, real estate financing, investment properties, transformations. We distinguish ourselves by being fast, flexible, and personal.

Please ensure the front has an attractive and inviting appearance, and leave space on the back for additional text.

Color codes: #E85B35 en #091E33

```html
<!DOCTYPE html>
<html lang="en">
<head>
<meta charset="utf-8">
<title>Dovrel – Real Estate &amp; Financing Postcard</title>
<link rel="stylesheet" href="https://fonts.googleapis.com/css2?family=Poppins:wght@400;500;600;700&display=swap">
<style>
  :root{
    --orange:#E85B35;
    --orange-deep:#c4461f;
    --navy:#091E33;
    --navy-light:#13305a;
    --white:#ffffff;
    --panel-grey:#d9dadc;
    --page:#d4d5d7;
  }
  *{box-sizing:border-box;margin:0;padding:0}
  html,body{width:682px;height:1200px;overflow:hidden}
  body{background:var(--page);font-family:"Poppins",sans-serif;position:relative}
  .card{position:absolute;left:60px;width:562px;height:351px;overflow:hidden;box-shadow:-4px 5px 8px rgba(0,0,0,.35)}
  .card--front{top:228px}
  .card--back{top:621px;background:var(--white)}
  .card svg.shapes{position:absolute;inset:0;width:562px;height:351px}
  .abs{position:absolute}
  .brand{display:flex;align-items:center;gap:5px;font-weight:700;color:var(--navy);line-height:1}
  .brand__dot{width:9px;height:9px;border-radius:50%;background:var(--orange)}
  .front-brand{left:19px;top:26px;font-size:40px}
  .front-title{left:19px;top:90px;font-size:20.5px;font-weight:600;color:var(--white);letter-spacing:.1px}
  .tag{display:inline-block;border:1.2px solid var(--white);border-radius:3px;color:var(--white);line-height:1}
  .what-we-do{left:19px;top:123px;background:var(--navy);font-size:9.5px;font-weight:500;padding:3px 6px}
  .services{left:19px;top:146px;width:300px;display:grid;grid-template-columns:145px 150px;row-gap:4px;color:var(--white);font-size:9px}
  .service{display:flex;align-items:center;gap:6px;height:14px;white-space:nowrap}
  .service__icon{width:13px;height:13px;border-radius:50%;border:1px solid var(--white);background:var(--navy);display:flex;align-items:center;justify-content:center}
  .service__icon::after{content:"";width:5px;height:5px;border-radius:50%;border:1px solid var(--white)}
  .qualities{left:19px;top:209px;display:flex;gap:5px}
  .quality{background:var(--navy);font-size:12px;font-weight:500;padding:3px 10px 2px}
  .about-label{left:19px;top:261px;background:var(--orange);font-size:9px;font-weight:600;padding:3px 6px}
  .body-copy{color:var(--white);font-size:7.6px;line-height:9.4px;width:290px}
  .about-copy{left:19px;top:284px}
  .contact-heading{color:var(--orange);font-weight:600;letter-spacing:.2px}
  .phone{display:flex;align-items:center;gap:5px;font-weight:600}
  .front-contact-heading{left:362px;top:279px;font-size:9.5px}
  .front-phone{left:362px;top:292px;font-size:17px;color:var(--navy)}
  .front-links{left:362px;top:319px;display:flex;gap:9px;font-size:8px;color:var(--navy)}
  .link{display:flex;align-items:center;gap:4px;white-space:nowrap}
  .ico{width:11px;height:11px;border-radius:50%;background:var(--orange);display:flex;align-items:center;justify-content:center;flex:none}
  .ico svg{width:7px;height:7px}
  .additional-label{left:19px;top:30px;font-size:9.5px;font-weight:600;color:var(--white)}
  .additional-copy{left:19px;top:50px}
  .back-contact-heading{left:15px;top:232px;font-size:11px}
  .back-phone{left:15px;top:246px;font-size:17px;color:var(--white)}
  .back-links{left:15px;top:274px;display:flex;flex-direction:column;gap:5px;font-size:10px;color:var(--white)}
  .back-links .ico{width:13px;height:13px}
  .back-links .ico svg{width:8px;height:8px}
  .address{align-items:flex-start;line-height:12.5px}
  .back-brand{left:370px;top:40px;font-size:29px}
  .stamp-box{left:474px;top:16px;width:71px;height:70px;border:1px solid var(--navy)}
  .address-line{left:344px;width:200px;height:1px;background:var(--navy)}
</style>
</head>
<body>

<!-- FRONT -->
<section class="card card--front">
  <svg class="shapes" viewBox="0 0 562 351" aria-hidden="false">
    <defs>
      <linearGradient id="houseTones" x1="0" y1="0" x2="1" y2="1">
        <stop offset="0" stop-color="#c9cac6"/>
        <stop offset=".5" stop-color="#a9aaa3"/>
        <stop offset="1" stop-color="#5e5a4c"/>
      </linearGradient>
    </defs>
    <rect width="562" height="351" fill="var(--navy)"/>
    <polygon points="60,351 150,243 190,243 100,351" fill="var(--navy-light)" opacity=".45"/>
    <polygon points="180,351 270,243 300,243 210,351" fill="var(--navy-light)" opacity=".35"/>
    <rect x="0" y="0" width="300" height="80" fill="var(--white)"/>
    <path d="M0 80 H260 Q272 80 277 91 L350 243 H0 Z" fill="var(--orange)"/>
    <polygon points="322,243 352,243 336,283" fill="var(--orange-deep)"/>
    <path d="M343 270 H562 V339 H380 Q369 339 365 329 Z" fill="var(--panel-grey)"/>
    <path d="M248 0 H562 V270 H362 Q351 270 346 259 Z" fill="url(#houseTones)" role="img" aria-label="Photo of a smiling couple in front of their new house with a sold sign"/>
    <polygon points="487,0 562,0 562,176" fill="var(--orange)"/>
  </svg>

  <div class="abs brand front-brand"><span>Dovrel</span><span class="brand__dot"></span></div>
  <h1 class="abs front-title">Real Estate &amp; Financing</h1>
  <span class="abs tag what-we-do">What we do:</span>
  <ul class="abs services" style="list-style:none">
    <li class="service"><span class="service__icon"></span>Project financing</li>
    <li class="service"><span class="service__icon"></span>Real estate financing</li>
    <li class="service"><span class="service__icon"></span>Investment properties</li>
    <li class="service"><span class="service__icon"></span>Transformations</li>
    <li class="service"><span class="service__icon"></span>Temporary real estate financing</li>
  </ul>
  <div class="abs qualities">
    <span class="tag quality">Fast</span>
    <span class="tag quality">Flexible</span>
    <span class="tag quality">Personal</span>
  </div>
  <span class="abs tag about-label">About Us:</span>
  <p class="abs body-copy about-copy">Lorem ipsum dolor sit amet, consectetur adipiscing elit, sed do eiusmod tempor incididunt ut labore et dolore magna aliqua. Ut enim ad minim veniam, quis nostrud exercitation ullamco laboris nisi ut aliquip ex ea commodo consequat. Duis aute irure dolor in reprehenderit in voluptate velit esse cillum dolore eu fugiat nulla pariatur.</p>

  <h2 class="abs contact-heading front-contact-heading">CONTACT INFORMATION</h2>
  <div class="abs phone front-phone">
    <svg width="14" height="14" viewBox="0 0 24 24"><path d="M6.6 10.8a15.1 15.1 0 0 0 6.6 6.6l2.2-2.2a1 1 0 0 1 1-.25 11.4 11.4 0 0 0 3.6.57 1 1 0 0 1 1 1V20a1 1 0 0 1-1 1A17 17 0 0 1 3 4a1 1 0 0 1 1-1h3.5a1 1 0 0 1 1 1c0 1.25.2 2.45.57 3.6a1 1 0 0 1-.25 1z" fill="var(--navy)"/></svg>
    <span>(555) 214-3870</span>
  </div>
  <div class="abs front-links">
    <span class="link"><span class="ico"><svg viewBox="0 0 10 10"><circle cx="5" cy="5" r="4" fill="none" stroke="#fff"/><path d="M1 5h8M5 1v8" stroke="#fff"/></svg></span>www.dovrel.com</span>
    <span class="link"><span class="ico"><svg viewBox="0 0 10 10"><rect x="1" y="2" width="8" height="6" fill="none" stroke="#fff"/><path d="M1 2l4 3 4-3" fill="none" stroke="#fff"/></svg></span>info@dovrel.com</span>
  </div>
</section>

<!-- BACK -->
<section class="card card--back">
  <svg class="shapes" viewBox="0 0 562 351">
    <defs>
      <linearGradient id="savingsTones" x1="0" y1="0" x2="1" y2="1">
        <stop offset="0" stop-color="#8d9499"/><stop offset="1" stop-color="#e7e9ea"/>
      </linearGradient>
      <linearGradient id="handoverTones" x1="0" y1="0" x2="1" y2="1">
        <stop offset="0" stop-color="#d6dadb"/><stop offset="1" stop-color="#3c3f46"/>
      </linearGradient>
    </defs>
    <polygon points="0,0 331,0 231,351 0,351" fill="var(--navy)"/>
    <polygon points="0,0 331,0 284,167 0,167" fill="var(--orange)"/>
    <polygon points="39,127 156,127 132,211 16,211" fill="url(#savingsTones)" stroke="#fff" stroke-width="1.5" role="img" aria-label="Photo of a coin dropped into a piggy bank beside stacked coins"/>
    <polygon points="163,127 281,127 259,211 141,211" fill="url(#handoverTones)" stroke="#fff" stroke-width="1.5" role="img" aria-label="Photo of an agent handing house keys to a couple"/>
  </svg>

  <h2 class="abs additional-label">Additional Text:</h2>
  <p class="abs body-copy additional-copy">Lorem ipsum dolor sit amet, consectetur adipiscing elit, sed do eiusmod tempor incididunt ut labore et dolore magna aliqua. Ut enim ad minim veniam, quis nostrud exercitation ullamco laboris nisi ut aliquip ex ea commodo consequat. Duis aute irure dolor in reprehenderit in voluptate velit esse cillum dolore eu fugiat nulla pariatur.</p>

  <h2 class="abs contact-heading back-contact-heading">CONTACT INFORMATION</h2>
  <div class="abs phone back-phone">
    <svg width="14" height="14" viewBox="0 0 24 24"><path d="M6.6 10.8a15.1 15.1 0 0 0 6.6 6.6l2.2-2.2a1 1 0 0 1 1-.25 11.4 11.4 0 0 0 3.6.57 1 1 0 0 1 1 1V20a1 1 0 0 1-1 1A17 17 0 0 1 3 4a1 1 0 0 1 1-1h3.5a1 1 0 0 1 1 1c0 1.25.2 2.45.57 3.6a1 1 0 0 1-.25 1z" fill="#fff"/></svg>
    <span>(555) 214-3870</span>
  </div>
  <div class="abs back-links">
    <span class="link"><span class="ico"><svg viewBox="0 0 10 10"><circle cx="5" cy="5" r="4" fill="none" stroke="#fff"/><path d="M1 5h8M5 1v8" stroke="#fff"/></svg></span>www.dovrel.com</span>
    <span class="link"><span class="ico"><svg viewBox="0 0 10 10"><rect x="1" y="2" width="8" height="6" fill="none" stroke="#fff"/><path d="M1 2l4 3 4-3" fill="none" stroke="#fff"/></svg></span>info@dovrel.com</span>
    <span class="link address"><span class="ico"><svg viewBox="0 0 10 10"><path d="M5 9.5S2 6 2 4a3 3 0 0 1 6 0c0 2-3 5.5-3 5.5z" fill="#fff"/><circle cx="5" cy="4" r="1" fill="var(--orange)"/></svg></span><span>2180 Harbor Crest Lane 42<br>Millbrook Village, 40127</span></span>
  </div>

  <div class="abs brand back-brand"><span>Dovrel</span><span class="brand__dot" style="width:7px;height:7px"></span></div>
  <div class="abs stamp-box"></div>
  <div class="abs address-line" style="top:172px"></div>
  <div class="abs address-line" style="top:205px"></div>
  <div class="abs address-line" style="top:238px"></div>
</section>

</body>
</html>
```